Parcel Haven
Website design - Gifts and Occasions
Website design
Gifts and Occasions
The company is a gift giving service that helps people pick out the perfect gift based on an algorthim
above header
https://www.pallorby.net/
BrightMarkup BrightMarkup

```html
<!DOCTYPE html>
<html lang="en">
<head>
<meta charset="utf-8">
<title>Parcel Haven — Sign Up</title>
<link rel="stylesheet" href="https://fonts.googleapis.com/css2?family=Roboto:wght@400;500&family=Open+Sans:wght@400&display=swap">
<style>
  :root {
    --header-top: #8fd0d3;
    --header-bottom: #c4e8e9;
    --page-bg: #fbfefe;
    --footer-bg: #eef7f8;
    --footer-line: #d7ecee;
    --brand-brown: #7d5209;
    --button-brown: #8a5b0b;
    --field-border: #c9e5e6;
    --placeholder: #6f6f6f;
    --body-text: #3c3c3c;
    --accent-teal: #5ec0c4;
    --white: #ffffff;
  }
  * { box-sizing: border-box; margin: 0; padding: 0; }
  html, body { width: 1200px; height: 787px; overflow: hidden; }
  body {
    position: relative;
    background: var(--page-bg);
    font-family: "Roboto", sans-serif;
    color: var(--body-text);
  }
  .site-header {
    position: absolute; left: 0; top: 0; width: 1200px; height: 113px;
    background: linear-gradient(to bottom, var(--header-top), var(--header-bottom));
  }
  .brand {
    position: absolute; left: 139px; top: 10px; width: 96px; height: 96px;
    background: var(--white);
    display: flex; align-items: center; justify-content: center; text-align: center;
    font-family: "Roboto", sans-serif; font-weight: 500; font-size: 15px; line-height: 1.2;
    color: var(--accent-teal);
  }
  .login-label {
    position: absolute; top: 22px; font-size: 15px; color: var(--white);
  }
  .field {
    position: absolute; height: 36px; background: var(--white);
    border: 1px solid var(--field-border);
    font-size: 16px; color: var(--placeholder);
    padding-left: 10px; display: flex; align-items: center;
  }
  .login-field { top: 41px; height: 37px; border: none; }
  .button {
    position: absolute; background: var(--button-brown); color: var(--white);
    display: flex; align-items: center; justify-content: center;
  }
  .login-button { left: 989px; top: 41px; width: 70px; height: 37px; font-size: 16px; }

  .about-title, .signup-title {
    position: absolute; color: var(--brand-brown); font-weight: 400;
  }
  .about-title { left: 142px; top: 169px; font-size: 32px; }
  .about-text {
    position: absolute; left: 142px; width: 410px;
    font-family: "Open Sans", sans-serif; font-size: 15.5px; line-height: 30px; color: var(--body-text);
  }
  .signup-title { left: 598px; top: 140px; font-size: 42px; }

  .select::after {
    content: ""; position: absolute; right: 10px; top: 15px;
    border-left: 8px solid transparent; border-right: 8px solid transparent;
    border-top: 9px solid var(--accent-teal);
  }
  .group-label { position: absolute; left: 598px; font-size: 18px; color: var(--body-text); }
  .radio {
    position: absolute; top: 512px; display: flex; align-items: center; gap: 12px;
    font-size: 16px; color: var(--body-text);
  }
  .radio-dot {
    width: 19px; height: 19px; border-radius: 50%;
    border: 1px solid #8d8d8d; background: var(--white);
  }
  .signup-button { left: 598px; top: 631px; width: 112px; height: 37px; font-size: 21px; font-weight: 500; }

  .site-footer {
    position: absolute; left: 0; top: 708px; width: 1200px; height: 79px;
    background: var(--footer-bg); border-top: 1px solid var(--footer-line);
  }
  .footer-line { position: absolute; left: 142px; font-size: 13.5px; color: var(--accent-teal); }
</style>
</head>
<body>
  <header class="site-header">
    <div class="brand">Parcel<br>Haven</div>
    <span class="login-label" style="left:598px">User Name</span>
    <div class="field login-field" style="left:598px;width:186px"></div>
    <span class="login-label" style="left:794px">Password</span>
    <div class="field login-field" style="left:794px;width:186px"></div>
    <div class="button login-button">Log in</div>
  </header>

  <section>
    <h2 class="about-title">About Us</h2>
    <p class="about-text" style="top:211px">Parcel Haven is a gift giving service that recommends the best gift for your personal or professional relationship. We will organize your upcoming events and notify you if a gift may need to be sent.</p>
    <p class="about-text" style="top:357px">Parcel Haven utilizes complex computer algorithms to recommend you a gift.</p>
  </section>

  <section>
    <h1 class="signup-title">Sign Up</h1>
    <div class="field" style="left:598px;top:206px;width:225px">First Name</div>
    <div class="field" style="left:833px;top:206px;width:226px">Last Name</div>
    <div class="field" style="left:598px;top:252px;width:461px">Email</div>
    <div class="field" style="left:598px;top:297px;width:461px">User Name</div>
    <div class="field" style="left:598px;top:343px;width:225px">Password</div>
    <div class="field" style="left:833px;top:343px;width:226px">Re-enter Password</div>
    <div class="field select" style="left:598px;top:388px;width:461px">Security Question</div>
    <div class="field" style="left:598px;top:434px;width:461px">Answer</div>

    <span class="group-label" style="top:486px">Gender</span>
    <label class="radio" style="left:598px"><span class="radio-dot"></span>Male</label>
    <label class="radio" style="left:676px"><span class="radio-dot"></span>Female</label>

    <span class="group-label" style="top:539px">Birthday</span>
    <div class="field select" style="left:598px;top:566px;width:147px">Month</div>
    <div class="field select" style="left:754px;top:566px;width:149px">Day</div>
    <div class="field select" style="left:912px;top:566px;width:147px">Year</div>

    <div class="button signup-button">SIGN UP</div>
  </section>

  <footer class="site-footer">
    <span class="footer-line" style="top:16px">Parcel Haven © 2014</span>
    <span class="footer-line" style="top:45px">English (US)</span>
  </footer>
</body>
</html>
```